Sonoma County Winery needs a fresh label design for new line of natural wines

The growing natural wine market requires a fresh perspective. Traditional wine labels don't attract the attention of natural wine buyers or the spirit for which they were made. Natural wines tend to be sustainable, organic and biodynamic. Natural wines also break norms and have disrupted the commercial wine industry with their non-traditional imagery and label designs. Natural wines stick out on the shelf for their brighter colors, illustrations and more handwritten font selections. Bottles are typically flint (clear glass) showing the true color of the wine, red and white. Red wines are typically not opaque, but rather light colored with zero filtration (
see attached pic). No capsule is used, therefore, the cork is shown through the glass bottle.

Target Market(s)

Wine buyers between the ages of 21-35 generally living in large cities, but more specifically San Francisco and Los Angeles

Requirements
Must have
• Dimensions:2 3/4 Inches Wide5 1/4 Inches TallIntended to print on Bright White Felt paper CMYK
Nice to have
• It may not have any words on the front label at all. It's more about symbolism and color and design then it is about the actual brand name (which will go on the back where all the legal stuff is). I've included several bottle shots from natural winemakers that may give you a sense that there is no one way to design a natural wine label, but rather several directions at this early stage in the market cycle
Should not have
• If it looks and smells like a traditional wine label, it's probably not the right idea

```html
<!DOCTYPE html>
<html lang="en">
<head>
<meta charset="utf-8">
<title>Natural Wine Label</title>
<link rel="stylesheet" href="https://fonts.googleapis.com/css2?family=Montserrat:wght@300;500&display=swap">
<style>
  :root {
    --wine-red: #8c1519;
    --wine-red-deep: #6e0d10;
    --wine-red-light: #9a2a2c;
    --paper-cream: #f8f4ec;
    --label-charcoal: #2e2624;
    --blush-pink: #f4d6d8;
    --heading-white: #f3ecea;
  }
  * { margin: 0; padding: 0; box-sizing: border-box; }
  html, body { width: 1200px; height: 720px; overflow: hidden; }
  body {
    position: relative;
    background: radial-gradient(ellipse at 30% 20%, var(--wine-red-light) 0%, var(--wine-red) 50%, var(--wine-red-deep) 100%);
    font-family: "Montserrat", sans-serif;
  }
  .presentation-title {
    position: absolute;
    top: 49px;
    left: 0;
    width: 1200px;
    text-align: center;
    font-weight: 300;
    font-size: 15px;
    line-height: 18px;
    letter-spacing: 0.55em;
    padding-left: 0.55em;
    color: var(--heading-white);
  }
  .wine-label {
    position: absolute;
    left: 454px;
    top: 107px;
    width: 291px;
    height: 555px;
    border-radius: 146px;
    background: var(--paper-cream);
    overflow: hidden;
  }
  .label-panel {
    position: absolute;
    left: 22px;
    top: 41px;
    width: 247px;
    height: 471px;
    border-radius: 124px;
    background: var(--label-charcoal);
    overflow: hidden;
  }
  .label-tagline {
    position: absolute;
    top: 85px;
    left: 0;
    width: 100%;
    text-align: center;
    font-weight: 500;
    font-size: 8px;
    line-height: 10px;
    letter-spacing: 0.62em;
    padding-left: 0.62em;
    color: var(--blush-pink);
  }
  .label-name {
    position: absolute;
    top: 226px;
    left: 0;
    width: 100%;
    text-align: center;
    font-weight: 500;
    font-size: 14px;
    line-height: 18px;
    letter-spacing: 0.3em;
    padding-left: 0.3em;
    color: var(--blush-pink);
  }
  .vineyard-sketch {
    position: absolute;
    left: 65px;
    top: 356px;
    width: 114px;
    height: 66px;
    border-radius: 40% 45% 35% 40%;
    background: radial-gradient(ellipse at center, rgba(244, 214, 216, 0.45) 0%, rgba(244, 214, 216, 0.2) 55%, rgba(46, 38, 36, 0) 75%);
  }
  .grain {
    position: absolute;
    inset: 0;
    width: 100%;
    height: 100%;
    pointer-events: none;
  }
  .grain-canvas { opacity: 0.22; }
  .grain-paper { opacity: 0.28; }
  .grain-panel { opacity: 0.16; }
</style>
</head>
<body>
  <svg class="grain grain-canvas" aria-hidden="true">
    <filter id="grain-fine">
      <feTurbulence type="fractalNoise" baseFrequency="0.95" numOctaves="2" stitchTiles="stitch"/>
      <feColorMatrix values="0 0 0 0 0  0 0 0 0 0  0 0 0 0 0  0 0 0 1.6 -0.55"/>
    </filter>
    <filter id="grain-light">
      <feTurbulence type="fractalNoise" baseFrequency="0.9" numOctaves="2" stitchTiles="stitch"/>
      <feColorMatrix values="0 0 0 0 1  0 0 0 0 1  0 0 0 0 1  0 0 0 1.6 -0.6"/>
    </filter>
    <rect width="100%" height="100%" filter="url(#grain-fine)"/>
  </svg>

  <h1 class="presentation-title">LABEL DESIGN</h1>

  <div class="wine-label">
    <svg class="grain grain-paper" aria-hidden="true">
      <rect width="100%" height="100%" filter="url(#grain-fine)"/>
    </svg>
    <div class="label-panel">
      <svg class="grain grain-panel" aria-hidden="true">
        <rect width="100%" height="100%" filter="url(#grain-light)"/>
      </svg>
      <p class="label-tagline">LOREM IPSUM DOLOR</p>
      <p class="label-name">OSSA</p>
      <div class="vineyard-sketch" role="img" aria-label="Hand-drawn pink line sketch of a hillside vineyard with rows of vines and a farmhouse"></div>
    </div>
  </div>
</body>
</html>
```